Business Cards for wirefen.com.au
Logo already designed by Quillnoxa
Professional
Liam Forbury
Technical Engineer
Mobile: 0437 125 806
liam@wirefen.com.au
www.wirefen.com.au
Should have the text: "Cloud Application Development"

```html
<!DOCTYPE html>
<html lang="en">
<head>
<meta charset="utf-8">
<title>wirefen.com.au business cards</title>
<link rel="stylesheet" href="https://fonts.googleapis.com/css2?family=Roboto:wght@400;700&display=swap">
<style>
  :root {
    --page: #ebe8e3;
    --card: #ffffff;
    --ink: #2f3237;
    --muted: #6c7078;
    --blue: #1b5fb3;
    --blue-light: #3f8ad8;
    --band-grey: #44474d;
    --ghost: #e6edf5;
  }
  * { margin: 0; padding: 0; box-sizing: border-box; }
  html, body { width: 1200px; height: 799px; overflow: hidden; }
  body {
    background: var(--page);
    font-family: "Roboto", Arial, sans-serif;
    color: var(--ink);
    position: relative;
  }
  .card {
    position: absolute;
    width: 520px;
    height: 300px;
    background: var(--card);
    border-radius: 22px;
    overflow: hidden;
    box-shadow: 0 4px 14px rgba(0,0,0,0.12);
  }
  .card--a { left: 50px; top: 75px; }
  .card--b { left: 630px; top: 75px; }
  .card--c { left: 50px; top: 425px; }
  .card--d { left: 630px; top: 425px; }

  .corner-band { position: absolute; top: 0; right: 0; width: 520px; height: 300px; }

  .ghost-circle {
    position: absolute;
    width: 150px; height: 150px;
    border-radius: 50%;
    background: var(--ghost);
  }

  .brand { position: absolute; }
  .brand__name {
    display: flex;
    align-items: center;
    gap: 8px;
    font-size: 40px;
    font-weight: 700;
    color: var(--ink);
    letter-spacing: -0.5px;
    line-height: 1;
  }
  .brand__dot {
    width: 22px; height: 22px;
    border-radius: 50%;
    background: var(--blue);
    flex: none;
  }
  .brand__tagline {
    margin-top: 4px;
    text-align: right;
    font-size: 11px;
    color: var(--blue);
  }

  .person { position: absolute; }
  .person__name { font-size: 15px; font-weight: 700; color: var(--blue); }
  .person__role { font-size: 10px; color: var(--muted); margin-top: 2px; }

  .contact { position: absolute; font-size: 10.5px; line-height: 1.55; color: var(--ink); }
  .contact__label { font-weight: 700; color: var(--blue); }
</style>
</head>
<body>

  <!-- Card A -->
  <section class="card card--a">
    <svg class="corner-band" viewBox="0 0 520 300" aria-hidden="true">
      <defs>
        <linearGradient id="blueA" x1="0" y1="0" x2="1" y2="1">
          <stop offset="0" stop-color="#3f8ad8"/><stop offset="1" stop-color="#163f86"/>
        </linearGradient>
      </defs>
      <path d="M350 0 L395 0 Q490 60 520 155 L520 185 Q470 65 350 0 Z" fill="#44474d"/>
      <path d="M395 0 L520 0 L520 155 Q490 60 395 0 Z" fill="url(#blueA)"/>
    </svg>
    <div class="ghost-circle" style="left:-30px; top:190px;"></div>
    <div class="brand" style="left:22px; top:88px;">
      <div class="brand__name"><span class="brand__dot"></span>wirefen.com.au</div>
      <div class="brand__tagline">Cloud Application Development</div>
    </div>
    <div class="person" style="left:200px; top:160px;">
      <div class="person__name">Liam Forbury</div>
      <div class="person__role">Technical Engineer</div>
    </div>
    <div class="contact" style="left:200px; top:215px;">
      <div><span class="contact__label">Mobile :</span> 0437 125 806</div>
      <div><span class="contact__label">Email :</span> liam@wirefen.com.au</div>
      <div><span class="contact__label">Web :</span> www.wirefen.com.au</div>
    </div>
  </section>

  <!-- Card B -->
  <section class="card card--b">
    <svg class="corner-band" viewBox="0 0 520 300" aria-hidden="true">
      <defs>
        <linearGradient id="blueB" x1="0" y1="0" x2="1" y2="1">
          <stop offset="0" stop-color="#3f8ad8"/><stop offset="1" stop-color="#163f86"/>
        </linearGradient>
      </defs>
      <path d="M350 0 L395 0 Q490 60 520 155 L520 185 Q470 65 350 0 Z" fill="#44474d"/>
      <path d="M395 0 L520 0 L520 155 Q490 60 395 0 Z" fill="url(#blueB)"/>
    </svg>
    <div class="ghost-circle" style="left:400px; top:190px;"></div>
    <div class="brand" style="left:24px; top:58px;">
      <div class="brand__name"><span class="brand__dot"></span>wirefen.com.au</div>
      <div class="brand__tagline">Cloud Application Development</div>
    </div>
    <div class="person" style="left:60px; top:170px;">
      <div class="person__name">Liam Forbury</div>
      <div class="person__role">Technical Engineer</div>
    </div>
    <div class="contact" style="left:230px; top:165px;">
      <div><span class="contact__label">Mobile :</span> 0437 125 806</div>
      <div><span class="contact__label">Email :</span> liam@wirefen.com.au</div>
      <div><span class="contact__label">Web :</span> www.wirefen.com.au</div>
    </div>
  </section>

  <!-- Card C -->
  <section class="card card--c">
    <svg class="corner-band" viewBox="0 0 520 300" aria-hidden="true">
      <defs>
        <linearGradient id="blueC" x1="0" y1="0" x2="1" y2="1">
          <stop offset="0" stop-color="#3f8ad8"/><stop offset="1" stop-color="#163f86"/>
        </linearGradient>
      </defs>
      <path d="M350 0 L395 0 Q490 60 520 155 L520 185 Q470 65 350 0 Z" fill="#44474d"/>
      <path d="M395 0 L520 0 L520 155 Q490 60 395 0 Z" fill="url(#blueC)"/>
    </svg>
    <div class="ghost-circle" style="left:-40px; top:110px;"></div>
    <div class="brand" style="left:110px; top:60px;">
      <div class="brand__name"><span class="brand__dot"></span>wirefen.com.au</div>
      <div class="brand__tagline">Cloud Application Development</div>
    </div>
    <div class="person" style="left:110px; top:175px;">
      <div class="person__name">Liam Forbury</div>
      <div class="person__role">Technical Engineer</div>
    </div>
    <div class="contact" style="left:250px; top:170px;">
      <div><span class="contact__label">Mobile :</span> 0437 125 806</div>
      <div><span class="contact__label">Email :</span> liam@wirefen.com.au</div>
      <div><span class="contact__label">Web :</span> www.wirefen.com.au</div>
    </div>
  </section>

  <!-- Card D -->
  <section class="card card--d">
    <svg class="corner-band" viewBox="0 0 520 300" aria-hidden="true">
      <defs>
        <linearGradient id="blueD" x1="0" y1="0" x2="1" y2="1">
          <stop offset="0" stop-color="#3f8ad8"/><stop offset="1" stop-color="#163f86"/>
        </linearGradient>
      </defs>
      <path d="M350 0 L395 0 Q490 60 520 155 L520 185 Q470 65 350 0 Z" fill="#44474d"/>
      <path d="M395 0 L520 0 L520 155 Q490 60 395 0 Z" fill="url(#blueD)"/>
    </svg>
    <div class="ghost-circle" style="left:390px; top:150px;"></div>
    <div class="person" style="left:30px; top:28px;">
      <div class="person__name">Liam Forbury</div>
      <div class="person__role">Technical Engineer</div>
    </div>
    <div class="brand" style="left:95px; top:100px;">
      <div class="brand__name"><span class="brand__dot"></span>wirefen.com.au</div>
      <div class="brand__tagline">Cloud Application Development</div>
    </div>
    <div class="contact" style="left:30px; top:215px;">
      <div><span class="contact__label">Mobile :</span> 0437 125 806</div>
      <div><span class="contact__label">Email :</span> liam@wirefen.com.au</div>
      <div><span class="contact__label">Web :</span> www.wirefen.com.au</div>
    </div>
  </section>

</body>
</html>
```